Website on Hubspot CMS -Boutique consulting firm focused on the events and event tech industries

Design website for our business using Hubspot CMS. Some pages already done. We would like those tweaked to match your recommended design. We also would like landing pages created for four business services offerings. We have a color palette and logo.

Our current website can be found here: www.q7mallianz.co

Q7M Partners has four service lines:
1. Outsourced Sales
2. Lantern Yard Strategic Consulting
3. Plinvo Strategic Consulting
4. Q7M VIP

Target Market(s)

event organizers, media companies, corporate event marketers, event tech organizations

Industry/Entity Type

Consulting

Coding

Coded - Design and coding required

Number of Pages Required

5+ page

Font styles to use
Sans Serif

Requirements
Must have
• This will be a website built using Hubspot CMS. If you are not familiar with this, please do not participate as we will not be able to use your designs.
SEO optimized
Landing pages with lead capture leading to content downloads
Each service line needs its own page/s with cta's
Highly visual, modern, bold
Navigational areas: Home, Services, Resources, Events, Blog, About Us
Content formats: video, podcasts, content downloads
Will need at least 4 landing pages in addition to the website for each service line plus templates in case we need to update with new copy
We have or own color palette and logo as well as logos for Lantern Yard and Plinvo. Those colors must be used.
Font can be modified
We need to have a conversation with the designer that is chosen to go over each service line and also understand what kind of images we should be uploading.
Nice to have
• We would really like the site to reflect the following words:
Bold
Future focused
Results oriented
Hyper focused on the events and event technology sectors (sub sectors: corporate event marketers and B2B media companies).
Should not have
• Flat one page design

```html
<!DOCTYPE html>
<html lang="en">
<head>
<meta charset="utf-8">
<title>Plinvo — Digital Strategy for Event Organizers</title>
<link href="https://fonts.googleapis.com/css2?family=Poppins:wght@500;600;700;800&family=Lato:wght@400;700&display=swap" rel="stylesheet">
<style>
:root{
  --orange:#ff4a0a;
  --ink:#111;
  --text:#444;
  --muted:#6b6b6b;
  --grey:#f1f1f1;
  --line:#dcdcdc;
  --white:#fff;
}
*{box-sizing:border-box;margin:0;padding:0}
html,body{width:1200px;height:2877px;overflow:hidden}
body{position:relative;background:var(--white);font-family:'Lato',sans-serif;color:var(--text)}
.abs{position:absolute}
.brand{display:flex;align-items:center;gap:6px;font-family:'Poppins',sans-serif;font-weight:600;color:#333;letter-spacing:1px}
.brand .dot{width:12px;height:12px;border-radius:50%;background:var(--orange)}
.site-header{left:0;top:0;width:1200px;height:85px;background:var(--white);border-bottom:1px solid #eee}
.main-nav{left:339px;top:35px;display:flex;gap:28px;font-family:'Poppins',sans-serif;font-weight:600;font-size:11.5px;letter-spacing:.3px;color:var(--ink)}
.main-nav .active{color:var(--orange)}
.social{display:flex;gap:14px}
.social span{width:11px;height:11px;border-radius:50%;background:#8a8a8a;display:block}
.partner-name{font-family:'Poppins',sans-serif;font-weight:600;color:var(--orange);font-size:20px}
.hero{left:0;top:85px;width:1200px;height:494px;background:linear-gradient(100deg,#c9c6c2 0%,#a8a29b 35%,#7d7c80 60%,#bcbcbf 100%)}
.hero-title{right:107px;top:253px;width:600px;text-align:right;font-family:'Poppins',sans-serif;font-weight:800;font-size:25px;line-height:30px;color:var(--white)}
.btn-dark{right:107px;top:364px;width:183px;height:46px;border:2px solid var(--orange);border-radius:3px;background:#2a2523;color:#fff;font-family:'Poppins',sans-serif;font-weight:700;font-size:13px;display:flex;align-items:center;justify-content:center;box-shadow:0 6px 18px rgba(255,74,10,.45)}
.intro-text{left:284px;top:684px;width:780px;font-family:'Poppins',sans-serif;font-weight:600;font-size:17.5px;line-height:22px;color:var(--ink)}
.services{left:0;top:853px;width:1200px;height:561px;background:var(--grey)}
.section-title{font-family:'Poppins',sans-serif;font-weight:700;font-size:29px;color:var(--ink)}
.lead{font-size:11.5px;line-height:17px;color:var(--text)}
.btn-orange{background:var(--orange);color:#fff;font-family:'Poppins',sans-serif;font-weight:700;font-size:13px;border-radius:3px;display:flex;align-items:center;justify-content:center;box-shadow:0 8px 18px rgba(255,74,10,.4)}
.tile{width:160px;text-align:center}
.tile .box{width:84px;height:84px;margin:0 auto;background:#fff;display:flex;align-items:center;justify-content:center}
.tile p{margin-top:16px;font-family:'Poppins',sans-serif;font-weight:500;font-size:12.5px;color:#333}
.card{width:311px;height:412px;background:#fff;box-shadow:0 4px 20px rgba(0,0,0,.06)}
.card .photo{height:211px;position:relative}
.card .date{position:absolute;left:0;top:0;width:72px;height:52px;background:var(--orange);color:#fff;font-family:'Poppins',sans-serif;font-weight:600;line-height:1;padding:12px 0 0 22px;clip-path:polygon(0 0,100% 0,100% 60%,70% 100%,0 100%)}
.card .date small{display:block;font-size:11px}
.card .date b{font-size:17px}
.card h3{margin:24px 19px 0;font-family:'Poppins',sans-serif;font-weight:700;font-size:14px;color:var(--ink)}
.card p{margin:14px 19px 0;font-size:11.5px;line-height:17px;color:var(--text)}
.card .more{margin:18px 19px 0;font-family:'Poppins',sans-serif;font-weight:700;font-size:11px;color:var(--orange);display:flex;align-items:center;gap:8px}
.contact-bg{left:0;top:2067px;width:776px;height:501px;background:var(--grey)}
.field{background:#fff;font-family:'Poppins',sans-serif;font-weight:600;font-size:11.5px;color:#222;padding:17px 15px}
.btn-outline{border:2px solid var(--orange);border-radius:3px;background:#fff;color:var(--orange);font-family:'Poppins',sans-serif;font-weight:700;font-size:11px;display:flex;align-items:center;justify-content:center;box-shadow:0 8px 18px rgba(255,74,10,.3)}
.contact-card{left:706px;top:2162px;width:388px;height:310px;background:var(--orange);color:#fff;padding:40px 0 0 114px;font-family:'Poppins',sans-serif}
.contact-card h2{font-weight:700;font-size:27px;margin-bottom:22px}
.contact-card .row{display:flex;gap:8px;font-weight:600;font-size:13.5px;line-height:21px;margin-bottom:20px}
.foot-title{font-family:'Poppins',sans-serif;font-weight:700;font-size:11px;color:var(--orange);padding-bottom:8px;border-bottom:1px solid var(--line)}
.foot-list{list-style:none;margin-top:14px;font-family:'Poppins',sans-serif;font-weight:500;font-size:11px;line-height:16.5px;color:#222}
.copyright{left:0;top:2837px;width:1200px;text-align:center;font-family:'Poppins',sans-serif;font-weight:600;font-size:9px;color:#555}
</style>
</head>
<body>

<header class="site-header abs">
  <div class="brand abs" style="left:68px;top:31px;font-size:18px"><span class="dot"></span>plinvo</div>
  <nav class="main-nav abs">
    <span class="active">HOME</span><span>ABOUT PLINVO</span><span>SERVICES</span><span>BLOG</span><span>CONTACT</span>
  </nav>
  <svg class="abs" style="left:786px;top:35px" width="15" height="15" viewBox="0 0 15 15"><circle cx="6" cy="6" r="4.5" fill="none" stroke="#111" stroke-width="2"/><line x1="9.5" y1="9.5" x2="13.5" y2="13.5" stroke="#111" stroke-width="2"/></svg>
  <div class="partner-name abs" style="left:835px;top:28px">Q7M</div>
  <div class="abs" style="left:930px;top:28px;width:1px;height:28px;background:var(--line)"></div>
  <div class="social abs" style="left:967px;top:37px"><span></span><span></span><span></span><span></span><span></span></div>
</header>

<section class="hero abs" role="img" aria-label="Photo of smiling business professionals talking together in a bright office"></section>
<h1 class="hero-title abs">Comprehensive Digital Strategy, Technology Selection, Implementation and Go-to-Market Advisory for Event Organizers.</h1>
<div class="btn-dark abs">LEARN MORE</div>

<section>
  <div class="brand abs" style="left:105px;top:700px;font-size:26px"><span class="dot" style="width:18px;height:18px"></span>plinvo</div>
  <p class="intro-text abs">Plinvo, a partnership between Brightvane Consulting and Q7M Partners, is a comprehensive digital strategy, technology selection, implementation and go-to-market advisory for event organizers.</p>
</section>

<section class="services abs">
  <h2 class="section-title abs" style="left:107px;top:83px">What Plinvo Does</h2>
  <p class="lead abs" style="left:107px;top:136px;width:460px">Lorem ipsum dolor sit amet, consectetur adipiscing elit, sed do eiusmod tempor inci didunt ut labore et dolore magna aliqua. Ut enim ad minim veniam, quis nostrud ex ercitation ullamco laboris nisi ut aliquip ex ea commodo consequat. Duis aute irure dolor in reprehenderit in voluptate velit esse cillum dolore eu fugiat nulla pariatur.</p>
  <div class="btn-orange abs" style="left:105px;top:225px;width:157px;height:40px">LEARN MORE</div>

  <div class="tile abs" style="left:625px;top:85px"><div class="box"><svg width="52" height="48" viewBox="0 0 52 48" fill="none" stroke="#ff4a0a" stroke-width="2"><rect x="4" y="4" width="44" height="34" rx="2"/><line x1="2" y1="42" x2="50" y2="42"/><circle cx="16" cy="22" r="3"/><circle cx="36" cy="28" r="3"/><path d="M19 22h10l4 6"/></svg></div><p>Digital Strategy</p></div>
  <div class="tile abs" style="left:784px;top:85px"><div class="box"><svg width="52" height="50" viewBox="0 0 52 50" fill="none" stroke="#ff4a0a" stroke-width="2"><rect x="4" y="8" width="36" height="34" rx="2"/><line x1="4" y1="17" x2="40" y2="17"/><line x1="13" y1="3" x2="13" y2="11"/><line x1="31" y1="3" x2="31" y2="11"/><circle cx="38" cy="36" r="10" fill="#fff"/><path d="M38 30v6l4 3"/></svg></div><p>Event Architecture</p></div>
  <div class="tile abs" style="left:943px;top:85px"><div class="box"><svg width="56" height="56" viewBox="0 0 56 56" fill="none" stroke="#ff4a0a" stroke-width="5"><circle cx="28" cy="28" r="22" stroke-dasharray="14 6"/><circle cx="28" cy="28" r="11" stroke-width="3"/></svg></div><p>Technology Stack</p></div>

  <div class="tile abs" style="left:625px;top:222px"><div class="box"><svg width="54" height="50" viewBox="0 0 54 50" fill="none" stroke="#ff4a0a" stroke-width="3"><path d="M4 6h46v30H16l-8 8v-8H4z"/><circle cx="18" cy="21" r="1.5" fill="#ff4a0a"/><circle cx="27" cy="21" r="1.5" fill="#ff4a0a"/><circle cx="36" cy="21" r="1.5" fill="#ff4a0a"/></svg></div><p>Functional Review</p></div>
  <div class="tile abs" style="left:784px;top:222px"><div class="box"><svg width="46" height="56" viewBox="0 0 46 56" fill="none" stroke="#ff4a0a" stroke-width="2"><rect x="3" y="5" width="40" height="48" rx="2"/><g fill="#ff4a0a" stroke="none"><rect x="10" y="18" width="7" height="5"/><rect x="20" y="18" width="7" height="5"/><rect x="30" y="18" width="7" height="5"/><rect x="10" y="27" width="7" height="5"/><rect x="20" y="27" width="7" height="5"/><rect x="30" y="27" width="7" height="5"/><rect x="10" y="36" width="7" height="5"/><rect x="20" y="36" width="7" height="5"/><rect x="30" y="36" width="7" height="5"/></g></svg></div><p>Balanced Scorecard</p></div>
  <div class="tile abs" style="left:943px;top:222px"><div class="box"><svg width="54" height="58" viewBox="0 0 54 58" fill="none" stroke="#ff4a0a" stroke-width="2"><path d="M27 3l23 13v26L27 55 4 42V16z"/><text x="27" y="33" text-anchor="middle" font-family="Poppins,sans-serif" font-size="12" font-weight="600" fill="#ff4a0a" stroke="none">DEMO</text></svg></div><p>Demo Management</p></div>

  <div class="tile abs" style="left:625px;top:360px"><div class="box"><svg width="56" height="56" viewBox="0 0 56 56" fill="none" stroke="#ff4a0a" stroke-width="2"><circle cx="28" cy="28" r="8"/><circle cx="28" cy="28" r="3"/><path d="M28 4v12M28 40v12M4 28h12M40 28h12M11 11l8 8M37 37l8 8M45 11l-8 8M11 45l8-8"/></svg></div><p>Implementation</p></div>
  <div class="tile abs" style="left:784px;top:360px"><div class="box"><svg width="54" height="56" viewBox="0 0 54 56" fill="none" stroke="#ff4a0a" stroke-width="2"><rect x="4" y="10" width="34" height="42"/><path d="M12 46V36M19 46V30M26 46V38"/><circle cx="36" cy="22" r="11" fill="#fff"/><path d="M29 24l4-5 4 5 5-6"/><path d="M44 14l6-8"/></svg></div><p>Go-To-Market</p></div>
  <div class="tile abs" style="left:943px;top:360px"><div class="box"><svg width="56" height="56" viewBox="0 0 56 56" fill="none" stroke="#ff4a0a" stroke-width="2"><rect x="8" y="4" width="40" height="24"/><path d="M14 22l8-8 6 5 10-9"/><circle cx="12" cy="38" r="4"/><circle cx="28" cy="38" r="4"/><circle cx="44" cy="38" r="4"/><path d="M4 52c0-5 4-8 8-8s8 3 8 8M20 52c0-5 4-8 8-8s8 3 8 8M36 52c0-5 4-8 8-8s8 3 8 8"/></svg></div><p>Team Training</p></div>
</section>

<section>
  <h2 class="section-title abs" style="left:0;top:1497px;width:1200px;text-align:center">Latest Blog</h2>

  <article class="card abs" style="left:105px;top:1570px">
    <div class="photo" role="img" aria-label="Overhead photo of a team working with laptops around a wooden table" style="background:linear-gradient(135deg,#5b3d2c,#3a2a22 60%,#6a5040)"><div class="date"><small>Mar</small><b>20</b></div></div>
    <h3>Lorem Ipsum Dolor Sit Amet</h3>
    <p>Lorem ipsum dolor sit amet, consectetur adipis cing elit, sed do eiusmod tempor incididunt ut la bore et dolore magna aliqua. Ut enim ad minim veniam, quis nostrud exercitation ullamco labor nisi ut aliquip ex ea commodo consequat.</p>
    <div class="more"><svg width="12" height="10" viewBox="0 0 12 10" fill="none" stroke="#ff4a0a" stroke-width="1.6"><path d="M0 5h11M7 1l4 4-4 4"/></svg>READ MORE</div>
  </article>
  <article class="card abs" style="left:444px;top:1570px">
    <div class="photo" role="img" aria-label="Photo of colleagues meeting around a table in a plant-filled office" style="background:linear-gradient(135deg,#b8b59c,#7b7a66 50%,#d8c979)"><div class="date"><small>Mar</small><b>20</b></div></div>
    <h3>Lorem Ipsum Dolor Sit Amet</h3>
    <p>Lorem ipsum dolor sit amet, consectetur adipis cing elit, sed do eiusmod tempor incididunt ut la bore et dolore magna aliqua. Ut enim ad minim veniam, quis nostrud exercitation ullamco labor nisi ut aliquip ex ea commodo consequat.</p>
    <div class="more"><svg width="12" height="10" viewBox="0 0 12 10" fill="none" stroke="#ff4a0a" stroke-width="1.6"><path d="M0 5h11M7 1l4 4-4 4"/></svg>READ MORE</div>
  </article>
  <article class="card abs" style="left:783px;top:1570px">
    <div class="photo" role="img" aria-label="Photo of a business handshake across a desk" style="background:linear-gradient(135deg,#d9dcdf,#9fa5ac 55%,#e4e2df)"><div class="date"><small>Mar</small><b>20</b></div></div>
    <h3>Lorem Ipsum Dolor Sit Amet</h3>
    <p>Lorem ipsum dolor sit amet, consectetur adipis cing elit, sed do eiusmod tempor incididunt ut la bore et dolore magna aliqua. Ut enim ad minim veniam, quis nostrud exercitation ullamco labor nisi ut aliquip ex ea commodo consequat.</p>
    <div class="more"><svg width="12" height="10" viewBox="0 0 12 10" fill="none" stroke="#ff4a0a" stroke-width="1.6"><path d="M0 5h11M7 1l4 4-4 4"/></svg>READ MORE</div>
  </article>
</section>

<section>
  <div class="contact-bg abs"></div>
  <h2 class="section-title abs" style="left:107px;top:2137px">Contact Us</h2>
  <div class="field abs" style="left:105px;top:2195px;width:258px;height:49px">Name</div>
  <div class="field abs" style="left:377px;top:2195px;width:258px;height:49px">Email</div>
  <div class="field abs" style="left:105px;top:2258px;width:258px;height:49px">Telephone</div>
  <div class="field abs" style="left:377px;top:2258px;width:258px;height:49px">Subject</div>
  <div class="field abs" style="left:105px;top:2321px;width:530px;height:130px">Message</div>
  <div class="btn-outline abs" style="left:105px;top:2466px;width:128px;height:32px">SEND</div>

  <div class="contact-card abs">
    <h2>Contact Us</h2>
    <div class="row"><svg width="10" height="14" viewBox="0 0 10 14" style="margin-top:3px"><path d="M5 0a5 5 0 0 1 5 5c0 4-5 9-5 9S0 9 0 5a5 5 0 0 1 5-5z" fill="#fff"/><circle cx="5" cy="5" r="2" fill="#ff4a0a"/></svg><div>Q7M Partners, Inc.<br>48 Kestrel Quay<br>Suite #210<br>Harbor Point, FL</div></div>
    <div class="row"><svg width="11" height="12" viewBox="0 0 11 12" style="margin-top:4px"><path d="M2 0l3 3-1.5 2a7 7 0 0 0 3 3L8 7l3 3-2 2C4 12-1 6 0 2z" fill="#fff"/></svg><div>1800.555.0142</div></div>
    <div class="row"><svg width="11" height="9" viewBox="0 0 11 9" style="margin-top:6px"><rect width="11" height="9" fill="#fff"/><path d="M0 0l5.5 5L11 0" fill="none" stroke="#ff4a0a"/></svg><div>info@q7mpartners.co</div></div>
  </div>
</section>

<footer>
  <div class="brand abs" style="left:195px;top:2648px;font-size:22px"><span class="dot" style="width:16px;height:16px"></span>plinvo</div>
  <div class="social abs" style="left:177px;top:2746px"><span></span><span></span><span></span><span></span><span></span></div>

  <div class="abs" style="left:375px;top:2626px;width:103px">
    <div class="foot-title">NAVIGATION</div>
    <ul class="foot-list"><li>Home</li><li>About Plinvo</li><li>Services</li><li>Blog</li><li>Contact</li></ul>
  </div>
  <div class="abs" style="left:551px;top:2626px;width:259px">
    <div class="foot-title">SERVICES</div>
    <ul class="foot-list abs" style="left:0;top:22px"><li>Digital Strategy</li><li>Event Architecture</li><li>Technology Stack</li><li>Functional Review</li><li>Balanced Scorecard</li></ul>
    <ul class="foot-list abs" style="left:146px;top:22px"><li>Demo Management</li><li>Implementation</li><li>Go-To-Market</li><li>Team Training</li></ul>
  </div>
  <div class="abs" style="left:882px;top:2626px;width:142px">
    <div class="foot-title">NEWSLETTER</div>
    <div class="abs" style="left:0;top:37px;width:117px;height:25px;border:1px solid #ccc;font-family:'Poppins',sans-serif;font-weight:500;font-size:9.5px;color:#333;padding:6px 8px">Email Address</div>
    <div class="abs" style="left:117px;top:37px;width:25px;height:25px;background:var(--orange);display:flex;align-items:center;justify-content:center"><svg width="11" height="9" viewBox="0 0 12 10" fill="none" stroke="#fff" stroke-width="1.6"><path d="M0 5h11M7 1l4 4-4 4"/></svg></div>
    <div class="partner-name abs" style="left:0;top:94px;font-size:30px">Q7M</div>
  </div>

  <p class="copyright abs">© COPYRIGHT 2021 PLINVO - Q7M PARTNERS I ALL RIGHTS RESERVED</p>
</footer>

</body>
</html>
```